Bluewater Getaways KT needs a new Website

We have an old website that is just that - old. We need a fresh website that is professional graphic designed that has the following features.
1. Can be updated by ourselves in some areas.
2. Has a shopping cart.
3. Has links to download PDF files
4. Has links to other pages in the website
5. Includes social media links
6. Has a client log-in area
Full details in brief provided.

SORRY BUT IT'S URGENT. We've taken too long to write the details and it is now urgent. So my apologies I will be asking for designers to work quickly.

We will continue to use our existing web hosting company and url. Their is a link to the old website in the Design Brief.
Updates

UPDATE:  Please see the new file UPDATE TO DESIGN BRIEF.
Thanks for all your submissions to date.  We hope the update will assist with your designs.
As indicated in previous messages, we are happy with the Home Page + 1 Page in order to select the designer to work with in creating the full design. 

Thankyou Designers.  Much appreciate your efforts.
It's getting late here on Norfolk so I won't have much chance too review any more designs this evening.
But for your information:
Designer 7318405 Ravindra Mehta is so far the closest to what we are seeking.
Thanks again. 

Reason: Have extended to Monday 7 October to give time for designers to submit after feedback today. Especially given the time differences

Target Market(s)

Very wide audience. Current client group not that tech savvy, but we hope to broaden our market and sell more creative products, and so website needs to consider how people now use media, ie tablets & iphones.

Industry/Entity Type

Shopping

Requirements
Nice to have
• PLEASE SEE THE "UPDATE TO THE DESIGN BRIEF"

```html
<!DOCTYPE html>
<html lang="en">
<head>
<meta charset="utf-8">
<title>Bluewater Getaways KT</title>
<link rel="stylesheet" href="https://fonts.googleapis.com/css2?family=Ubuntu:ital,wght@0,300;0,400;0,500;1,400;1,500&family=Raleway:wght@400;500&display=swap">
<style>
:root{
  --orange:#e0701c;
  --rust:#c0652a;
  --green:#2f9a3a;
  --text:#333;
  --muted:#666;
  --line:#d6d6d6;
  --teal:#1f4c4b;
  --sea:#3cb9c4;
}
*{margin:0;padding:0;box-sizing:border-box}
html,body{width:964px;height:1200px;overflow:hidden;background:#fff}
body{position:relative;font-family:"Ubuntu",sans-serif;color:var(--text)}
.abs{position:absolute}
/* header */
.header-rule{position:absolute;height:1px;background:#aaa}
.brand{position:absolute;left:386px;top:22px;width:192px;display:flex;align-items:center;gap:8px}
.brand-mark{width:22px;height:22px;border-radius:50%;background:var(--orange);flex:none}
.brand-name{font-size:17px;font-weight:500;color:var(--orange);line-height:1.1}
/* hero */
.hero-side{position:absolute;top:88px;height:297px;width:188px;background:linear-gradient(180deg,#5f9c84 0%,#44c2c9 35%,#22a5b3 100%)}
.hero-main{position:absolute;left:188px;top:88px;width:587px;height:297px;background:linear-gradient(180deg,#2f74c6 0%,#7fb2e4 45%,#b49a7a 75%,#8a6f55 100%)}
.hero-title{position:absolute;left:188px;width:587px;text-align:center;color:#fff;font-size:17.5px;line-height:26px;top:107px}
.hero-title em{font-style:normal;color:#f0913a}
.dots{position:absolute;left:440px;top:369px;width:88px;height:24px;border-radius:12px;background:#fff;box-shadow:0 2px 4px rgba(0,0,0,.25);display:flex;justify-content:center;align-items:center;gap:6px}
.dots span{width:11px;height:11px;border-radius:50%;border:1px solid #bbb;background:#f2f2f2}
.dots span:first-child{background:#ccc}
/* columns */
.vrule{position:absolute;top:385px;width:1px;height:745px;background:var(--line)}
.nav{position:absolute;left:0;top:407px;width:188px;list-style:none}
.nav li{height:31px;border-bottom:1px dashed #bbb;text-align:right;padding-right:16px;font-size:9.5px;line-height:30px;color:#444}
.nav li.active{color:var(--orange)}
/* section headings */
.section-title{position:absolute;left:260px;width:444px;display:flex;align-items:center;gap:14px;font-family:"Raleway",sans-serif;font-size:17px;color:#333;white-space:nowrap}
.section-title::before,.section-title::after{content:"";flex:1;height:1px;background:#999}
/* promo cards */
.promo{position:absolute;top:459px;width:132px}
.promo-photo{position:absolute;top:11px;left:0;width:132px;height:94px;border:1px solid var(--rust)}
.promo-tag{position:absolute;top:0;left:21px;width:92px;height:22px;background:var(--rust);color:#fff;font-size:12.5px;text-align:center;line-height:22px;border-radius:2px}
.intro{position:absolute;left:204px;width:560px;text-align:center;font-size:11px;line-height:17px;color:#333}
.intro .tick{color:var(--green);font-weight:500}
.read-more{position:absolute;left:204px;width:560px;top:640px;text-align:center;font-style:italic;font-weight:500;font-size:11px;color:var(--rust)}
.quote{position:absolute;left:230px;width:520px;top:677px;text-align:center;font-size:11px;line-height:17px;color:#333}
.qmark{position:absolute;font-family:Georgia,serif;font-size:26px;color:#e8a96b;font-weight:bold}
/* gallery */
.gal-card{position:absolute;top:788px;width:158px;height:236px;border:1px solid #ddd;background:#fff}
.gal-photo{position:absolute;left:0;top:0;width:156px;height:120px}
.gal-body{position:absolute;left:4px;right:4px;top:120px;bottom:4px;background:#f2f2f2;text-align:center}
.gal-title{margin-top:14px;font-size:11.5px;color:var(--rust)}
.gal-text{margin:8px 10px 0;font-size:8.8px;line-height:13px;color:#555}
.arrow{position:absolute;top:898px}
/* sidebar */
.side-h{position:absolute;left:787px;font-size:11.5px;color:var(--rust)}
.side-rule{position:absolute;left:775px;top:433px;width:189px;height:1px;background:var(--line)}
.side-text{position:absolute;left:787px;font-size:8.7px;line-height:15.5px;color:#333}
.side-label{color:var(--rust);font-weight:500}
.video{position:absolute;left:787px;top:708px;width:144px;height:85px;border:1px solid #ddd;padding:4px;background:#fff}
.video-img{width:100%;height:100%;background:linear-gradient(180deg,#b3563c,#7b6a4c 70%,#5a5a3a)}
.play{position:absolute;left:60px;top:28px;width:26px;height:20px;background:rgba(0,0,0,.55);border-radius:3px}
.field{position:absolute;left:787px;width:142px;height:20px;border:1px solid #bbb;background:#f1f1f1;font-size:8.7px;color:#555;padding-left:5px;line-height:18px}
.btn{position:absolute;left:787px;top:930px;width:39px;height:20px;background:var(--rust);color:#fff;font-size:9px;text-align:center;line-height:20px}
.banner{position:absolute;left:787px;width:142px;border-radius:3px}
.banner-label{position:absolute;color:#fff;font-size:11px;font-weight:500;text-align:center;width:100%}
/* footer */
.footer{position:absolute;left:0;top:1130px;width:964px;height:70px;background:var(--teal);border-top:4px solid #b0572a;color:#e6ecea;text-align:center;font-size:9px;line-height:15px;padding-top:20px}
</style>
</head>
<body>

<header>
  <div class="header-rule" style="left:188px;top:48px;width:177px"></div>
  <div class="header-rule" style="left:243px;top:39px;width:122px"></div>
  <div class="header-rule" style="left:594px;top:48px;width:177px"></div>
  <div class="header-rule" style="left:594px;top:39px;width:122px"></div>
  <div class="brand"><span class="brand-mark"></span><span class="brand-name">Bluewater Getaways KT</span></div>
</header>

<section class="hero">
  <div class="hero-side" style="left:0" role="img" aria-label="Turquoise lagoon with pine-lined shore"></div>
  <div class="hero-side" style="left:775px" role="img" aria-label="Turquoise sea with rocky green headland"></div>
  <div class="hero-main" role="img" aria-label="Group of holiday guests riding camels along a beach"></div>
  <h1 class="hero-title" style="font-weight:400">Our <em>SOCIAL ENTERPRISE</em><br>Established July 2001</h1>
  <div class="dots"><span></span><span></span><span></span><span></span></div>
</section>

<div class="vrule" style="left:188px"></div>
<div class="vrule" style="left:775px"></div>

<ul class="nav">
  <li class="active">Home &raquo;</li>
  <li>Governance</li>
  <li>Kestrel Island</li>
  <li>Our Mission &amp; Values</li>
  <li>Services</li>
  <li>Our Facilitators</li>
  <li>Our Shop</li>
  <li>Holiday Programs</li>
  <li>Design your own Kestrel Island Holiday</li>
  <li>Wave Creative Projects</li>
  <li>Schoolies, Siblings &amp; Family Holidays</li>
  <li>Make a Booking</li>
  <li>Testimonials</li>
</ul>

<main>
  <h2 class="section-title" style="top:418px;font-weight:400">WE PROMOTES</h2>

  <div class="promo" style="left:204px">
    <div class="promo-photo" style="border-color:transparent;background:linear-gradient(180deg,#3d6e3a,#6fae45 60%,#c9a24a)" role="img" aria-label="Dancers in grass skirts on a lawn"></div>
    <div class="promo-tag">Diversity</div>
  </div>
  <div class="promo" style="left:349px">
    <div class="promo-photo" style="background:linear-gradient(180deg,#7a5a3e,#b2474a 55%,#4a3a34)" role="img" aria-label="Smiling group gathered at a celebration"></div>
    <div class="promo-tag">Caring</div>
  </div>
  <div class="promo" style="left:490px">
    <div class="promo-photo" style="background:linear-gradient(180deg,#6b5a4c,#cfcfcf 55%,#3d3535)" role="img" aria-label="Community group in white uniforms"></div>
    <div class="promo-tag">Community</div>
  </div>
  <div class="promo" style="left:631px">
    <div class="promo-photo" style="background:linear-gradient(180deg,#2c77b0,#4fb0cf 50%,#2b6f93)" role="img" aria-label="Kayaker paddling over clear blue water"></div>
    <div class="promo-tag">Kestrel Island</div>
  </div>

  <p class="intro" style="top:594px">We do for people requiring support to participate in socially inclusive events like;<br>
    <span class="tick">&#10003;</span> Holidays &nbsp; <span class="tick">&#10003;</span> Travel &nbsp; <span class="tick">&#10003;</span> Recreation &nbsp; <span class="tick">&#10003;</span> Respite &nbsp; <span class="tick">&#10003;</span> Creative projects</p>
  <a class="read-more">Read More &gt;&gt;</a>

  <span class="qmark" style="left:214px;top:668px">&ldquo;</span>
  <p class="quote">We specially care for people with Intellectual Disability, Acquired Brain Injury, Mental Health, Sensory Impairment, Frail Aged, Mobility Challenged, Siblings of children with Disabilities.</p>
  <span class="qmark" style="left:700px;top:692px">&rdquo;</span>

  <h2 class="section-title" style="top:750px;font-weight:400">OUR GALLERY</h2>

  <svg class="arrow" style="left:205px" width="12" height="20" viewBox="0 0 12 20"><path d="M10 2 L2 10 L10 18" fill="none" stroke="#c0652a" stroke-width="2"/></svg>
  <svg class="arrow" style="left:745px" width="12" height="20" viewBox="0 0 12 20"><path d="M2 2 L10 10 L2 18" fill="none" stroke="#c0652a" stroke-width="2"/></svg>

  <div class="gal-card" style="left:232px">
    <div class="gal-photo" style="background:linear-gradient(180deg,#5b7b4a,#8f9a63 50%,#b5946a)" role="img" aria-label="Guest feeding a kangaroo"></div>
    <div class="gal-body"><div class="gal-title">Image Title</div><p class="gal-text">Lorem ipsum dolor sit amet, consectetur adipisicing elit, sed do eiusmod tempor incididunt ut labore et dolore magna aliqua.</p></div>
  </div>
  <div class="gal-card" style="left:403px">
    <div class="gal-photo" style="top:4px;left:4px;width:148px;height:116px;background:linear-gradient(180deg,#3f8bd0,#7eb8e0 45%,#6b7a3e 75%,#3e4a33)" role="img" aria-label="Fisherman holding a large fish"></div>
    <div class="gal-body"><div class="gal-title">Image Title</div><p class="gal-text">Lorem ipsum dolor sit amet, consectetur adipisicing elit, sed do eiusmod tempor incididunt ut labore et dolore magna aliqua.</p></div>
  </div>
  <div class="gal-card" style="left:572px">
    <div class="gal-photo" style="top:4px;left:4px;width:148px;height:116px;background:linear-gradient(180deg,#9fc0d8,#8aa7b4 40%,#7b7570 75%,#5d5c5c)" role="img" aria-label="Group of friends seated by the sea"></div>
    <div class="gal-body"><div class="gal-title">Image Title</div><p class="gal-text">Lorem ipsum dolor sit amet, consectetur adipisicing elit, sed do eiusmod tempor incididunt ut labore et dolore magna aliqua.</p></div>
  </div>
</main>

<aside>
  <h3 class="side-h" style="top:411px;font-weight:400">Location &amp; Contacts</h3>
  <div class="side-rule"></div>
  <p class="side-text" style="top:447px">Harbour Lane, Coral Point<br>PO Box 614<br>Kestrel Island KT 4127<br>SOUTH PACIFIC<br>N.B.N. 517 204 866</p>
  <p class="side-text" style="top:535px"><span class="side-label">Telephone :</span><br>International + 61 55 30918<br>Australia 1800 431 662<br>New Zealand &nbsp;1800 431 662</p>
  <p class="side-text" style="top:613px"><span class="side-label">Email, Website &amp; Social :</span><br>hello@bluewatergetaways.org<br>www.bluewatergetaways.org<br>www.social.example/bluewatergetaways</p>

  <h3 class="side-h" style="top:688px;font-weight:400">Images &amp; Video</h3>
  <div class="video">
    <div class="video-img" role="img" aria-label="Video still of a guest in an outback landscape"></div>
    <svg class="play" viewBox="0 0 26 20"><path d="M10 5 L18 10 L10 15 Z" fill="#fff"/></svg>
  </div>
  <p class="side-text" style="top:797px;color:var(--rust);font-style:italic;font-weight:500">BLUEWATER VIDEO &gt;&gt;</p>
  <p class="side-text" style="top:813px;line-height:14px">To see more photographs and video's<br><span style="color:#3a6db3;font-style:italic">LIKE</span> &nbsp;our SOCIAL page.</p>

  <h3 class="side-h" style="top:859px;font-weight:400">Client Login</h3>
  <div class="field" style="top:881px">User id</div>
  <div class="field" style="top:906px">Password</div>
  <div class="btn">Login</div>
  <p class="side-text" style="top:932px;left:865px;text-decoration:underline;color:#555">Forget Password?</p>

  <div class="banner" style="top:969px;height:50px;background:linear-gradient(180deg,#5d6e3c,#8b8a4e 50%,#3f4a2c)" role="img" aria-label="Film festival promotion with dancers">
    <div class="banner-label" style="top:18px">WAVE FILM FESTIVAL</div>
  </div>

  <h3 class="side-h" style="top:1032px;font-weight:400">Support Us</h3>
  <div class="banner" style="top:1053px;height:50px;background:linear-gradient(90deg,#e9e2cc,#f5f1e4 50%,#d9cfb0);border:1px solid #d9d0b5" role="img" aria-label="Our shop button with leaf decoration">
    <div style="position:absolute;left:48px;top:4px;width:42px;height:42px;border-radius:50%;background:#fff;border:2px solid #8cb43a"></div>
    <div class="banner-label" style="top:12px;color:#4f6b1e;font-size:9.5px;line-height:12px">OUR<br>SHOP</div>
  </div>
</aside>

<footer class="footer">Copyright@2013, Bluewater Getaways<br>Terms &amp; Policy</footer>

</body>
</html>
```